Real Estate Agent needs business card design

We have logo designed already, want to have business card designed. Very interested in those smaller size business card as they look very trendy. Business name is called VORENDA REALTY

```html
<!DOCTYPE html>
<html lang="en">
<head>
<meta charset="utf-8">
<title>Vorenda Realty – Business Card</title>
<link rel="stylesheet" href="https://fonts.googleapis.com/css2?family=EB+Garamond:wght@400;500&display=swap">
<style>
  :root {
    --bg: #efeeef;
    --card-white: #ffffff;
    --card-black: #1e1e1e;
    --panel-dark: #141205;
    --gold: #b8901c;
    --ink: #111111;
    --ink-soft: #2a2a2a;
  }
  * { margin: 0; padding: 0; box-sizing: border-box; }
  html, body {
    width: 1200px;
    height: 955px;
    overflow: hidden;
    background: var(--bg);
    font-family: "EB Garamond", "Times New Roman", serif;
  }
  .sheet {
    width: 1200px;
    height: 955px;
    display: flex;
    flex-direction: column;
    align-items: center;
    justify-content: center;
    gap: 70px;
  }
  .card {
    width: 640px;
    height: 290px;
    box-shadow: 0 18px 30px rgba(0,0,0,0.18);
  }
  .card-front {
    background: var(--card-black);
    display: flex;
    align-items: center;
    justify-content: center;
  }
  .front-panel {
    width: 420px;
    height: 210px;
    background: var(--panel-dark);
    display: flex;
    align-items: center;
    justify-content: center;
    gap: 18px;
  }
  .brand-dot {
    width: 34px;
    height: 34px;
    border-radius: 50%;
    background: var(--gold);
  }
  .brand-name {
    color: var(--gold);
    font-weight: 500;
    font-size: 40px;
    letter-spacing: 2px;
  }
  .card-back {
    background: var(--card-white);
    display: flex;
    flex-direction: column;
    align-items: center;
    justify-content: center;
    text-align: center;
    color: var(--ink);
  }
  .agent-name {
    font-size: 30px;
    font-weight: 400;
    letter-spacing: 1px;
    line-height: 1;
  }
  .agent-role {
    font-size: 19px;
    color: var(--ink-soft);
    margin-top: 4px;
  }
  .agent-address {
    font-size: 18px;
    line-height: 1.2;
    margin-top: 20px;
  }
  .agent-contact {
    font-size: 18px;
    line-height: 1.2;
    margin-top: 18px;
  }
</style>
</head>
<body>
  <main class="sheet">
    <section class="card card-front" aria-label="Card front">
      <div class="front-panel">
        <span class="brand-dot" aria-hidden="true"></span>
        <span class="brand-name">VORENDA REALTY</span>
      </div>
    </section>
    <section class="card card-back" aria-label="Card back">
      <h1 class="agent-name">SIENNA MARLOWE</h1>
      <p class="agent-role">Senior Property Consultant</p>
      <p class="agent-address">7C, 48 Harbour Crescent,<br>Eastwood Bay, NSW 2190</p>
      <p class="agent-contact">0412 555 019<br>www.vorendarealty.com.au</p>
    </section>
  </main>
</body>
</html>
```